Book Cover Design Project

A non-fiction book on child protection, specifically... keeping young children safe from predators and keeping teenagers safe from themselves.

Title:
Beneath Our Roof

Subtitle:
A Guide To Keeping Your Children Safe

Author:
Martin Kellaway

```html
<!DOCTYPE html>
<html lang="en">
<head>
<meta charset="utf-8">
<title>Beneath Our Roof — Book Cover</title>
<link rel="stylesheet" href="https://fonts.googleapis.com/css2?family=Anton&display=swap">
<style>
  :root {
    --paper: #ffffff;
    --band: #c0c0c0;
    --ink: #111111;
    --title-light: #ffffff;
    --scene-top: #f4f3f7;
    --scene-bottom: #e6e6ea;
  }
  html, body {
    margin: 0;
    padding: 0;
    overflow: hidden;
    background: var(--paper);
  }
  .cover {
    position: relative;
    width: 912px;
    height: 1200px;
    overflow: hidden;
    background: var(--paper);
  }
  .cover-type {
    position: absolute;
    inset: 0;
  }
  .type {
    font-family: "Anton", "Oswald", Impact, sans-serif;
  }
  .title-light { fill: var(--title-light); }
  .title-dark { fill: var(--ink); }
  .subtitle, .author { fill: var(--ink); }
  .band { fill: var(--band); }
  .children-illustration {
    position: absolute;
    left: 345px;
    top: 800px;
    width: 567px;
    height: 376px;
    background: linear-gradient(180deg, var(--scene-top) 0%, var(--scene-bottom) 100%);
  }
</style>
</head>
<body>
<main class="cover">
  <div class="children-illustration" role="img" aria-label="Illustration of six children in a row dressed as a firefighter, doctor, nurse, police officer and other grown-up roles"></div>

  <svg class="cover-type" width="912" height="1200" viewBox="0 0 912 1200" xmlns="http://www.w3.org/2000/svg">
    <defs>
      <clipPath id="on-band" clipPathUnits="userSpaceOnUse"><rect x="0" y="0" width="197" height="1200"/></clipPath>
      <clipPath id="off-band" clipPathUnits="userSpaceOnUse"><rect x="197" y="0" width="715" height="1200"/></clipPath>
    </defs>

    <rect class="band" x="0" y="0" width="197" height="1200"/>

    <g class="book-title">
      <g clip-path="url(#on-band)">
        <text class="type title-light"
              transform="translate(236 1184) rotate(-90)"
              font-size="258" textLength="1140" lengthAdjust="spacingAndGlyphs">Beneath Our Roof</text>
      </g>
      <g clip-path="url(#off-band)">
        <text class="type title-dark"
              transform="translate(236 1184) rotate(-90)"
              font-size="258" textLength="1140" lengthAdjust="spacingAndGlyphs">Beneath Our Roof</text>
      </g>
    </g>

    <text class="type subtitle"
          transform="translate(328 1173) rotate(-90)"
          font-size="76" textLength="1124" lengthAdjust="spacingAndGlyphs">A Guide To Keeping Your Children Safe</text>

    <text class="type author" x="910" y="290" text-anchor="end"
          font-size="76" textLength="396" lengthAdjust="spacingAndGlyphs">Martin Kellaway</text>
  </svg>
</main>
</body>
</html>
```